Specialist Secondary Arts School needs a brochure to launch a new cheerleadingspecialism

We need a brochure design for launching a new cheer leading specialism as a part of Calderwood Academy of Performance (CAP)- a successful and unique secondary school program for gifted and aspiring artists. The specialism involves a partnership between CAP and Comets Elitesquad- the most successful cheerleading organisation in Australia. We believe this is a first in Australia and no other school based cheerleading program at this level exists. You can find out all about CAP at our website www.calderwoodacademyofperformance.example
The brochure should depict how unique and exciting this specialism is, whilst giving a general overview of CAP. It should also emphasize the partnership between CAP and Comet elitesquad.
You can find out all about Comets at their website www.cometselitesquad.example.au

```html
<!DOCTYPE html>
<html lang="en">
<head>
<meta charset="utf-8">
<title>Calderwood Academy of Performance – Cheer Brochure</title>
<link rel="stylesheet" href="https://fonts.googleapis.com/css2?family=Crimson+Text:ital,wght@0,400;0,600;1,400;1,700&family=Lobster&family=Yanone+Kaffeesatz:wght@400&display=swap">
<style>
  :root{
    --page-bg:#e9e9ec;
    --ink-blue:#2b3ea6;
    --ink-navy:#1c1f3a;
    --magenta:#d0178f;
    --violet:#7a3fc4;
    --sky:#3fb6f0;
    --royal:#1a55d8;
    --panel-a:#e4e8fb;
    --panel-b:#f4e7f6;
    --white:#ffffff;
  }
  *{margin:0;padding:0;box-sizing:border-box}
  html,body{width:1200px;height:626px;overflow:hidden;background:var(--page-bg)}
  .spread{
    position:absolute;left:228px;top:25px;width:658px;height:510px;
    transform:scale(1.13);transform-origin:0 0;background:var(--white);
    box-shadow:0 4px 18px rgba(0,0,0,.18);overflow:hidden;
    font-family:"Crimson Text",Georgia,serif;color:var(--ink-navy);
  }
  .spread-art{position:absolute;inset:0;width:658px;height:510px}
  .intro{
    position:absolute;left:12px;top:10px;width:205px;
    font-size:10.4px;line-height:12.6px;color:var(--ink-blue);
  }
  .event{position:absolute;left:0;width:232px;text-align:center;font-size:10.6px;line-height:12.4px}
  .event h2{font-style:italic;font-weight:700;color:var(--magenta);font-size:13px;line-height:15px}
  .event .venue{text-transform:uppercase}
  .event small{display:block;font-size:8.6px;line-height:10px}
  .event-first{top:88px}
  .event-second{top:171px}
  .event-third{top:274px}
  .contact-card{
    position:absolute;left:252px;top:236px;width:154px;height:142px;
    background:rgba(255,255,255,.94);border:2px solid var(--violet);border-radius:10px;
    text-align:center;padding-top:4px;font-style:italic;font-size:10.2px;line-height:12px;color:var(--ink-blue);
  }
  .contact-card .name{font-family:"Lobster",cursive;font-style:normal;font-size:16px;line-height:20px;color:var(--royal)}
  .contact-card svg{width:9px;height:9px;vertical-align:-1px;margin-right:3px}
  .contact-card .phone{margin-top:9px}
  .tagline{position:absolute;color:var(--white)}
  .tagline-title{left:458px;top:292px;font-family:"Yanone Kaffeesatz",sans-serif;font-size:27px;line-height:30px}
  .tagline-line{font-family:"Lobster",cursive;color:var(--ink-navy);font-size:15.5px;line-height:18px}
  .tagline-aim{left:436px;top:333px}
  .tagline-reap{left:494px;top:352px}
</style>
</head>
<body>
<main class="spread">
  <svg class="spread-art" viewBox="0 0 658 510" aria-hidden="false">
    <defs>
      <linearGradient id="panelFill" x1="0" y1="0" x2="1" y2="1">
        <stop offset="0" stop-color="var(--panel-a)"/><stop offset="1" stop-color="var(--panel-b)"/>
      </linearGradient>
      <linearGradient id="streak" x1="0" y1="0" x2="1" y2="0">
        <stop offset="0" stop-color="#f28ad8" stop-opacity=".1"/><stop offset="1" stop-color="#c04fe0" stop-opacity=".8"/>
      </linearGradient>
      <linearGradient id="heroPhoto" x1="0" y1="0" x2="1" y2="1">
        <stop offset="0" stop-color="#3a2a6a"/><stop offset=".45" stop-color="#c9507a"/><stop offset="1" stop-color="#2a1f55"/>
      </linearGradient>
      <linearGradient id="swoosh" x1="0" y1="0" x2="1" y2="0">
        <stop offset="0" stop-color="#7fd8f5"/><stop offset=".5" stop-color="#2f8ff0"/><stop offset="1" stop-color="#1a4fd0"/>
      </linearGradient>
      <linearGradient id="stunt" x1="0" y1="0" x2="1" y2="1">
        <stop offset="0" stop-color="#2c1c4a"/><stop offset="1" stop-color="#0d0a1e"/>
      </linearGradient>
      <radialGradient id="circleA"><stop offset="0" stop-color="#d9c9b8"/><stop offset="1" stop-color="#3a2e38"/></radialGradient>
      <radialGradient id="circleB"><stop offset="0" stop-color="#b8c9d9"/><stop offset="1" stop-color="#5b7a3a"/></radialGradient>
    </defs>
    <rect class="left-panel" width="300" height="510" fill="url(#panelFill)"/>
    <path class="panel-streak" d="M180 0 L225 0 L300 120 L270 125 Z" fill="url(#streak)" opacity=".6"/>
    <path class="panel-streak" d="M0 360 C80 380 180 400 300 370 L300 420 C180 440 80 430 0 410 Z" fill="#e9a6e6" opacity=".55"/>
    <path d="M215 0 H658 V228 C590 250 500 252 430 242 C340 230 290 210 250 190 C228 140 215 60 215 0 Z" fill="url(#heroPhoto)" role="img" aria-label="Photo of the cheer squad in pink costumes with pom-poms on stage"/>
    <path class="blue-swoosh" d="M230 190 C330 255 500 270 658 240 V345 C560 340 470 355 400 392 L300 392 C280 320 250 250 230 190 Z" fill="url(#swoosh)"/>
    <path class="white-wave" d="M270 260 C360 300 480 312 658 300 V330 C520 335 420 360 360 420 L300 420 Z" fill="#ffffff" opacity=".18"/>
    <path class="lower-sheen" d="M400 392 C470 355 560 340 658 345 V430 C580 400 500 395 430 405 Z" fill="#bfe9fb"/>
    <path d="M285 420 C330 396 420 386 555 386 V510 H285 Z" fill="url(#stunt)" role="img" aria-label="Photo of a cheer stunt pyramid at a championship"/>
    <circle cx="75" cy="440" r="49" fill="#fff"/>
    <circle cx="75" cy="440" r="46" fill="url(#circleA)" role="img" aria-label="Photo of cheer team members huddled together"/>
    <circle cx="187" cy="425" r="63" fill="#fff"/>
    <circle cx="187" cy="425" r="60" fill="url(#circleB)" role="img" aria-label="Group photo of the squad outdoors"/>
  </svg>

  <p class="intro">All competitions will be in Victoria and any other competition that are out of state will be up to the school to discuss this further with the parents. These are the 2014 dates 2015 dates will be announced closer to the end of 2014</p>

  <section class="event event-first">
    <h2>First Competition</h2>
    <p>Victoria, 8th evening Stunt,<br>9th &amp; 10th August (Melbourne) at the:</p>
    <p class="venue">Eastfield Sports Hall,</p>
    <p>120 Marlow Street, Eastfield South</p>
  </section>
  <section class="event event-second">
    <h2>Second Competition</h2>
    <p>Victoria, 19th evening Stunt,<br>20th &amp; 21st September (Melbourne) at the:</p>
    <p class="venue">Harbourside Aquatic<br>Centre,</p>
    <p>Linden Drive, Bayside Park</p>
    <small>(Hall A cheer &amp; Hall B dance,<br>both running 2 days)</small>
  </section>
  <section class="event event-third">
    <h2>Third Competition</h2>
    <p>Queensland,<br>28th- 30th November (Gold Coast) at the:</p>
    <p class="venue">Coastline Convention Centre,</p>
    <p>Seaview Highway, Sandbeach</p>
    <small>(Hall A cheer &amp; Hall B dance,<br>both running Saturday &amp; Sunday)</small>
  </section>

  <address class="contact-card">
    <p class="name">Dana Whitlock</p>
    <p><svg viewBox="0 0 10 10"><path d="M5 0a3.5 3.5 0 0 1 3.5 3.5C8.5 6 5 10 5 10S1.5 6 1.5 3.5A3.5 3.5 0 0 1 5 0z" fill="var(--violet)"/><circle cx="5" cy="3.5" r="1.3" fill="#fff"/></svg>CAP Administrator<br>Brookfield Secondary College<br>Eastern Campus,<br>Ashcombe Way<br>Brookfield 3999</p>
    <p class="phone"><svg viewBox="0 0 10 10"><path d="M2 0.5l2 2-1 1.3c.7 1.4 1.8 2.5 3.2 3.2l1.3-1 2 2-1.3 1.5C4.5 9.3.7 5.5.5 1.8z" fill="var(--violet)"/></svg>03 9000 1234</p>
    <p><svg viewBox="0 0 10 10"><circle cx="5" cy="5" r="4.5" fill="var(--violet)"/></svg>www.brookfieldsc.example.edu.au</p>
  </address>

  <h1 class="tagline tagline-title">Opportunities For All</h1>
  <p class="tagline tagline-line tagline-aim">Aim High,&nbsp; Embrace Learning</p>
  <p class="tagline tagline-line tagline-reap">Reap Rewards</p>
</main>
</body>
</html>
```